Personal training poster - 1200X900mm

Poster to promote my new personal training service at my gym. The poster will be printed and put into an aframe to be seen by people walking past my gym. It needs to be simple and eye catching with the text i have put in the must haves. The text and image should be the prominent parts of the design.

Target Market(s)

30-50 year old females

Industry/Entity Type

Fitness

Font styles to use
Sans Serif

Requirements
Must have
• my logo
• exercise graphic
• Must include the following text:
• Are you looking for a personal trainer? Our expert trainers can help you achieve you take your health and fitness back!
• Contact details:
• 1300452968
• info@brightmovegym.com.au
• Located under the Harbourview Club

```html
<!DOCTYPE html>
<html lang="en">
<head>
<meta charset="utf-8">
<title>Personal Training Poster</title>
<link rel="stylesheet" href="https://fonts.googleapis.com/css2?family=Alfa+Slab+One&family=Anton&family=Rubik:wght@400;500;700;900&family=Roboto+Slab:wght@400;700&display=swap">
<style>
  :root {
    --page-bg: #ececec;
    --poster-dark: #141414;
    --photo-mid: #4a4a4a;
    --photo-light: #8a8a8a;
    --accent-yellow: #fcd527;
    --band-red: #9b0a06;
    --alert-red: #e1251b;
    --text-white: #ffffff;
    --ink: #1a1a1a;
  }
  * { margin: 0; padding: 0; box-sizing: border-box; }
  html, body {
    width: 1038px;
    height: 1200px;
    overflow: hidden;
    background: var(--page-bg);
  }
  .poster {
    position: absolute;
    left: 93px;
    top: 18px;
    width: 851px;
    height: 1164px;
    background: var(--poster-dark);
    overflow: hidden;
  }
  .poster__photo {
    position: absolute;
    inset: 0;
    background:
      radial-gradient(ellipse 42% 40% at 78% 30%, var(--photo-light) 0%, rgba(90,90,90,0.5) 45%, transparent 75%),
      radial-gradient(ellipse 35% 30% at 85% 82%, var(--photo-mid) 0%, transparent 70%),
      radial-gradient(ellipse 25% 30% at 8% 72%, #3a3a3a 0%, transparent 70%),
      linear-gradient(160deg, #1c1c1c 0%, #2a2a2a 55%, #161616 100%);
  }
  .headline__are-you {
    position: absolute;
    left: 56px;
    top: 44px;
    font-family: "Alfa Slab One", serif;
    font-size: 70px;
    line-height: 1;
    color: var(--accent-yellow);
    letter-spacing: 1px;
  }
  .headline__looking {
    position: absolute;
    left: 56px;
    top: 110px;
    font-family: "Anton", sans-serif;
    font-size: 122px;
    line-height: 1;
    color: var(--text-white);
    letter-spacing: 3px;
  }
  .headline__band {
    position: absolute;
    left: 38px;
    top: 247px;
    width: 510px;
    height: 222px;
  }
  .headline__for-a {
    position: absolute;
    left: 48px;
    top: 455px;
    transform: rotate(-90deg);
    transform-origin: left top;
    font-family: "Alfa Slab One", serif;
    font-size: 52px;
    line-height: 1;
    color: var(--accent-yellow);
    letter-spacing: 4px;
  }
  .headline__word {
    position: absolute;
    left: 130px;
    font-family: "Alfa Slab One", serif;
    font-size: 120px;
    line-height: 1;
    color: var(--accent-yellow);
  }
  .headline__pers { top: 240px; }
  .headline__onal { top: 355px; }
  .headline__trainer {
    position: absolute;
    left: 58px;
    top: 478px;
    font-family: "Alfa Slab One", serif;
    font-size: 80px;
    line-height: 1;
    color: var(--text-white);
  }
  .intro {
    position: absolute;
    left: 82px;
    top: 596px;
    font-family: "Rubik", sans-serif;
    font-size: 36px;
    line-height: 46px;
    color: var(--text-white);
  }
  .intro__lead { color: var(--accent-yellow); }
  .brand {
    position: absolute;
    left: 0;
    width: 100%;
    top: 880px;
    display: flex;
    justify-content: center;
    align-items: center;
    gap: 16px;
  }
  .brand__dot {
    width: 34px;
    height: 34px;
    border-radius: 50%;
    background: var(--accent-yellow);
  }
  .brand__name {
    font-family: "Rubik", sans-serif;
    font-weight: 700;
    font-size: 52px;
    color: var(--text-white);
  }
  .contact-band {
    position: absolute;
    left: 0;
    bottom: 0;
    width: 100%;
    height: 116px;
  }
  .contact {
    position: absolute;
    left: 0;
    bottom: 0;
    width: 100%;
    height: 106px;
  }
  .contact__phone-icon {
    position: absolute;
    left: 34px;
    top: 28px;
  }
  .contact__label {
    position: absolute;
    left: 104px;
    top: 22px;
    font-family: "Rubik", sans-serif;
    font-weight: 700;
    font-size: 19px;
    color: var(--ink);
  }
  .contact__phone {
    position: absolute;
    left: 102px;
    top: 40px;
    font-family: "Rubik", sans-serif;
    font-weight: 900;
    font-size: 48px;
    letter-spacing: -1px;
    color: var(--ink);
  }
  .contact__mail-icon {
    position: absolute;
    left: 463px;
    top: 38px;
  }
  .contact__email {
    position: absolute;
    left: 500px;
    top: 28px;
    font-family: "Roboto Slab", serif;
    font-weight: 700;
    font-size: 26px;
    color: var(--ink);
  }
  .contact__location {
    position: absolute;
    left: 500px;
    top: 64px;
    font-family: "Roboto Slab", serif;
    font-size: 20px;
    color: var(--ink);
  }
</style>
</head>
<body>
  <main class="poster">
    <div class="poster__photo" role="img" aria-label="Black and white photo of a woman in a sports top training with a barbell, with athletes doing push-ups and crouching in a smoky gym behind her"></div>

    <div class="headline__are-you">ARE YOU</div>
    <div class="headline__looking">LOOKING</div>

    <svg class="headline__band" viewBox="0 0 510 222" aria-hidden="true">
      <path d="M6 14 L40 8 L120 12 L260 4 L400 10 L500 6 L506 60 L498 120 L508 180 L496 216 L380 210 L240 218 L110 212 L14 218 L4 160 L10 100 Z" fill="var(--band-red)"/>
    </svg>
    <div class="headline__for-a">FOR A</div>
    <div class="headline__word headline__pers">PERS</div>
    <div class="headline__word headline__onal">ONAL</div>
    <div class="headline__trainer">TRAINER?</div>

    <p class="intro">
      <span class="intro__lead">Our expert trainers can</span><br>
      help you achieve you take<br>
      your health and fitness back!
    </p>

    <div class="brand">
      <span class="brand__dot"></span>
      <span class="brand__name">BrightMove Gym</span>
    </div>

    <svg class="contact-band" viewBox="0 0 851 116" preserveAspectRatio="none" aria-hidden="true">
      <path d="M0 14 L60 8 L140 12 L230 2 L330 10 L430 4 L540 12 L640 6 L740 12 L851 4 L851 116 L0 116 Z" fill="var(--accent-yellow)"/>
    </svg>

    <div class="contact">
      <svg class="contact__phone-icon" width="58" height="58" viewBox="0 0 58 58" aria-hidden="true">
        <rect x="10" y="0" width="48" height="58" rx="4" fill="var(--alert-red)"/>
        <rect x="0" y="10" width="8" height="4" fill="var(--alert-red)"/>
        <rect x="0" y="22" width="8" height="4" fill="var(--alert-red)"/>
        <rect x="0" y="34" width="8" height="4" fill="var(--alert-red)"/>
        <rect x="0" y="46" width="8" height="4" fill="var(--alert-red)"/>
        <path d="M24 12 C20 14 19 22 24 32 C29 42 36 48 41 46 L44 41 L37 35 L33 38 C30 36 27 31 26 27 L30 24 L28 14 Z" fill="var(--text-white)"/>
      </svg>
      <div class="contact__label">Contact Us:</div>
      <div class="contact__phone">1300 452 968</div>

      <svg class="contact__mail-icon" width="28" height="18" viewBox="0 0 28 18" aria-hidden="true">
        <rect x="0" y="0" width="28" height="18" fill="var(--alert-red)"/>
        <path d="M1 1 L14 10 L27 1" fill="none" stroke="var(--accent-yellow)" stroke-width="2"/>
      </svg>
      <div class="contact__email">info@brightmovegym.com.au</div>
      <div class="contact__location">Located under the Harbourview Club</div>
    </div>
  </main>
</body>
</html>
```